Cell phone repair

you can please design me business card

size 3.5" x 2"

colors blue and red

fixit rapid logo (you get from my website fixitrapidco.example )

"We Come To You!

It is very simple! You tell us what phone you have, And we come to fix it."

phone number: 555.248.3906

website: www.fixitrapidco.example

email: info@fixitrapidco.example

```html
<!DOCTYPE html>
<html lang="en">
<head>
<meta charset="utf-8">
<title>Fixit Rapid – Business Card</title>
<link href="https://fonts.googleapis.com/css2?family=Open+Sans:ital,wght@0,400;0,600;0,700;1,700&display=swap" rel="stylesheet">
<style>
  :root {
    --backdrop: #2b2c30;
    --card-white: #ffffff;
    --navy: #164a82;
    --navy-deep: #0d3363;
    --sky: #3aaee3;
    --red: #e8283a;
    --ink: #222222;
  }
  * { box-sizing: border-box; margin: 0; padding: 0; }
  html, body {
    width: 1200px;
    height: 900px;
    overflow: hidden;
    background: var(--backdrop);
    font-family: "Open Sans", Arial, sans-serif;
  }
  .sheet {
    position: relative;
    width: 1200px;
    height: 900px;
  }
  .card {
    position: absolute;
    top: 300px;
    width: 525px;
    height: 300px;
    border-radius: 22px;
    overflow: hidden;
    box-shadow: 0 18px 40px rgba(0, 0, 0, 0.45);
  }
  .card--front { left: 45px; background: var(--card-white); }
  .card--back {
    left: 630px;
    background: radial-gradient(ellipse at 45% 45%, var(--navy) 0%, var(--navy-deep) 100%);
  }
  .edge-band {
    position: absolute;
    left: 0;
    bottom: 0;
    width: 100%;
    height: 30px;
  }
  .front-copy {
    position: absolute;
    left: 0;
    top: 28px;
    width: 100%;
    text-align: center;
  }
  .front-copy__lead {
    font-size: 14px;
    font-weight: 600;
    color: var(--ink);
  }
  .front-copy__headline {
    margin-top: 8px;
    font-size: 20px;
    font-weight: 700;
    font-style: italic;
    color: var(--sky);
  }
  .brand-name {
    font-weight: 700;
    color: var(--sky);
    display: inline-flex;
    align-items: center;
    gap: 10px;
  }
  .brand-name__dot {
    display: inline-block;
    border-radius: 50%;
    background: var(--red);
  }
  .front-brand {
    position: absolute;
    left: 0;
    top: 110px;
    width: 100%;
    text-align: center;
    font-size: 26px;
  }
  .front-brand .brand-name__dot { width: 16px; height: 16px; }
  .front-tagline {
    position: absolute;
    left: 0;
    top: 166px;
    width: 100%;
    text-align: center;
    font-size: 24px;
    font-weight: 700;
    font-style: italic;
    color: var(--red);
  }
  .front-contact {
    position: absolute;
    left: 0;
    bottom: 44px;
    width: 100%;
    text-align: center;
    font-size: 14px;
    font-weight: 600;
    color: var(--ink);
    white-space: nowrap;
  }
  .back-brand {
    position: absolute;
    left: 0;
    top: 110px;
    width: 100%;
    text-align: center;
    font-size: 44px;
  }
  .back-brand .brand-name__dot { width: 26px; height: 26px; }
</style>
</head>
<body>
<main class="sheet">

  <section class="card card--front" aria-label="Card front">
    <div class="front-copy">
      <p class="front-copy__lead">You tell us what phone you have, And we come to fix it.</p>
      <p class="front-copy__headline">It is very simple!</p>
    </div>
    <div class="front-brand">
      <span class="brand-name">Fixit Rapid<span class="brand-name__dot"></span></span>
    </div>
    <p class="front-tagline">We Come To You!</p>
    <p class="front-contact">555.248.3906 &nbsp;|&nbsp; fixitrapidco.example &nbsp;|&nbsp; info@fixitrapidco.example</p>
    <svg class="edge-band" viewBox="0 0 525 30" preserveAspectRatio="none">
      <polygon points="0,0 260,0 250,30 0,30" fill="var(--red)"/>
      <polygon points="266,0 525,0 525,30 256,30" fill="var(--sky)"/>
    </svg>
  </section>

  <section class="card card--back" aria-label="Card back">
    <div class="back-brand">
      <span class="brand-name">Fixit Rapid<span class="brand-name__dot"></span></span>
    </div>
    <svg class="edge-band" viewBox="0 0 525 30" preserveAspectRatio="none">
      <polygon points="0,0 150,0 140,30 0,30" fill="var(--red)"/>
      <polygon points="156,0 525,0 525,30 146,30" fill="var(--sky)"/>
    </svg>
  </section>

</main>
</body>
</html>
```